Sophrologist needs a cool signage at door entrance

I need signage for dr in sophrology based in Belgium (french speaking). The signed should capture the name the "Mireille Vantoorn" - "Naturopathe-Sophrologue-Reiki" and a catchphrase = (Healthy way of life)
« Fais du bien à ton corps, pour que ton âme ait envie d’y rester »
Requirements
Must have
- Hey,
Thats the instagram account for some inspiration www.instagram.com/mireille_serene_wellbeing
Light colors, green, blue
Healthy way of life
Size is 45cm wide on 30 cm high
The signage will be placed in front off woof pannel

```html
<!DOCTYPE html>
<html lang="fr">
<head>
<meta charset="utf-8">
<title>Mireille Vantoorn – Naturopathe-Sophrologue-Reiki</title>
<link rel="stylesheet" href="https://fonts.googleapis.com/css2?family=Bodoni+Moda:opsz,wght@6..96,500;6..96,700&family=Andika&display=swap">
<style>
  :root {
    --page: #ffffff;
    --sign: #fdfdfd;
    --frame: #3a3a3a;
    --green-deep: #4e663f;
    --green-leaf: #7f9b4e;
    --green-soft: #c9d3a8;
    --green-pale: #e6ebd4;
    --cream: #ffffff;
  }
  * { margin: 0; padding: 0; box-sizing: border-box; }
  html, body {
    width: 1200px;
    height: 854px;
    overflow: hidden;
    background: var(--page);
  }
  .signage { display: block; width: 1200px; height: 854px; }
  .name-first { font-family: "Bodoni Moda", serif; font-weight: 700; fill: var(--green-deep); }
  .name-last  { font-family: "Bodoni Moda", serif; font-weight: 700; fill: var(--green-leaf); }
  .disciplines { font-family: "Bodoni Moda", serif; font-weight: 500; fill: var(--green-deep); }
  .motto { font-family: "Andika", sans-serif; fill: var(--cream); }
</style>
</head>
<body>
<svg class="signage" viewBox="0 0 1200 854" xmlns="http://www.w3.org/2000/svg">
  <defs>
    <linearGradient id="vine-tone" x1="0" y1="0" x2="0" y2="1">
      <stop offset="0" stop-color="var(--green-pale)"/>
      <stop offset="1" stop-color="var(--green-soft)" stop-opacity="0.6"/>
    </linearGradient>
  </defs>

  <!-- sign panel -->
  <rect class="sign-panel" x="104.5" y="95.5" width="963" height="642" fill="var(--sign)" stroke="var(--frame)" stroke-width="0.8"/>

  <!-- floral vine corner -->
  <rect class="vine-corner" x="790" y="96" width="277" height="488" fill="url(#vine-tone)" role="img" aria-label="Arabesques de vigne végétale avec fleurs et feuilles vertes"/>

  <!-- name -->
  <text class="name-first" x="241" y="308" font-size="128" textLength="441" lengthAdjust="spacingAndGlyphs">Mireille</text>
  <line class="name-rule" x1="104" y1="436" x2="362" y2="436" stroke="var(--green-leaf)" stroke-width="2"/>
  <text class="name-last" x="359" y="437" font-size="128" textLength="436" lengthAdjust="spacingAndGlyphs">Vantoorn</text>

  <!-- disciplines -->
  <text class="disciplines" x="138" y="544" font-size="50" textLength="714" lengthAdjust="spacingAndGlyphs">Naturopathe-Sophrologue-Reiki</text>

  <!-- motto band -->
  <rect class="motto-band" x="104" y="602" width="964" height="136" fill="var(--green-leaf)"/>
  <rect class="sprig sprig-left" x="141" y="584" width="110" height="36" rx="6" fill="var(--green-soft)" role="img" aria-label="Brin de feuillage décoratif"/>
  <rect class="sprig sprig-right" x="912" y="584" width="110" height="36" rx="6" fill="var(--green-soft)" role="img" aria-label="Brin de feuillage décoratif"/>
  <text class="motto" x="586" y="654" font-size="44" text-anchor="middle" textLength="500" lengthAdjust="spacingAndGlyphs">Fais du bien à ton corps,</text>
  <text class="motto" x="586" y="710" font-size="44" text-anchor="middle" textLength="767" lengthAdjust="spacingAndGlyphs">pour que ton âme ait envie d’y rester</text>
</svg>
</body>
</html>
```